Hot sauce company needs a logo and label design- simple, clean & fresh

Toby K's a hot pepper sauce company based on the edge of London needs a logo and label design .
The sauces are handmade in small batches with natural ingredients , no added sugars or extracts and so we would like a clean fresh label to reflect this - avoiding all the macho devil and flames novelty stuff.
At present there are four sauces - Jalapeno ,Chipotle,Habanero and Reaper we would like to have one Toby K's label with the name of the sauce being changeable allowing us to react to what ingredients are available .
Updates

Project Deadline Extended
Reason: Hi Guys I have received a few requests to extend the deadline on the project and so I am thanks Toby K's

Target Market(s)

people who care what they eat

Industry/Entity Type

Food Store

Logo Text

Toby K's handmade hot sauce

Requirements
Must have
• Toby K's handmade hot sauce - or the logo
• the name of the sauce ie jalapeno
• no added sugars
Nice to have
• handmade
• small batch
Should not have
• cartoon men with smoke coming out of their ears
• devils and the flames of hell

```html
<!DOCTYPE html>
<html lang="en">
<head>
<meta charset="utf-8">
<title>Toby K's Handmade Hot Sauce – Jalapeno Label</title>
<link rel="stylesheet" href="https://fonts.googleapis.com/css2?family=Alfa+Slab+One&family=Pathway+Gothic+One&family=Ultra&display=swap">
<style>
  :root {
    --ink: #000000;
    --paper: #ffffff;
    --chilli: #c8232c;
    --chilli-bright: #e31b23;
    --chilli-deep: #7a0f14;
    --pattern-dark: #2a0a0c;
    --speck: rgba(255, 255, 255, 0.55);
    --speck-soft: rgba(255, 255, 255, 0.28);
    --slab: "Ultra", "Alfa Slab One", "Rockwell Extra Bold", serif;
    --gothic: "Pathway Gothic One", "Arial Narrow", sans-serif;
  }
  * { margin: 0; padding: 0; box-sizing: border-box; }
  html, body { width: 1200px; height: 842px; overflow: hidden; background: var(--paper); }

  .label {
    position: relative;
    width: 1200px;
    height: 842px;
    background: var(--ink);
    overflow: hidden;
  }

  /* distressed speckle texture shared by black field and red bands */
  .grunge {
    background-image:
      radial-gradient(circle at 20% 30%, var(--speck) 0 1.2px, transparent 1.8px),
      radial-gradient(circle at 70% 60%, var(--speck-soft) 0 1px, transparent 1.6px),
      radial-gradient(circle at 45% 85%, var(--speck) 0 0.8px, transparent 1.4px),
      radial-gradient(ellipse 3px 1.2px at 80% 15%, var(--speck-soft) 0 60%, transparent 100%),
      radial-gradient(circle at 10% 70%, var(--speck-soft) 0 1.5px, transparent 2.2px);
    background-size: 37px 41px, 53px 29px, 23px 47px, 61px 67px, 89px 73px;
  }

  .pepper-strip {
    position: absolute;
    top: 0;
    width: 68px;
    height: 842px;
    background: linear-gradient(180deg, var(--pattern-dark), #4a1014 50%, var(--pattern-dark));
  }
  .pepper-strip--left { left: 0; }
  .pepper-strip--right { left: 757px; width: 69px; }

  .red-band {
    position: absolute;
    top: 0;
    height: 842px;
    background-color: var(--chilli);
  }
  .red-band--left { left: 68px; width: 80px; }
  .red-band--right { left: 680px; width: 77px; }

  .front {
    position: absolute;
    left: 148px;
    top: 0;
    width: 532px;
    height: 842px;
    text-align: center;
    background-color: var(--ink);
  }

  .brand {
    position: absolute;
    left: 47px;
    top: 44px;
    width: 433px;
    height: 272px;
    display: flex;
    align-items: center;
    justify-content: center;
    gap: 16px;
    font-family: var(--slab);
    font-weight: 400;
    font-size: 54px;
    line-height: 1;
    color: var(--paper);
    white-space: nowrap;
  }
  .brand__square {
    width: 40px;
    height: 40px;
    background: var(--chilli-bright);
    flex: none;
  }

  .product-title {
    position: absolute;
    left: 0;
    top: 330px;
    width: 532px;
    font-family: var(--slab);
    font-weight: 400;
    font-size: 66px;
    line-height: 58px;
    letter-spacing: 0.1em;
    color: var(--paper);
  }
  .product-title span {
    display: block;
    height: 58px;
    transform: scaleX(1.25);
    transform-origin: center;
    white-space: nowrap;
  }
  .product-title .hot { color: var(--chilli); }

  .chilli-art {
    position: absolute;
    left: 150px;
    top: 572px;
    width: 200px;
    height: 148px;
    border-radius: 20% 70% 55% 60% / 30% 60% 70% 50%;
    background: radial-gradient(ellipse at 55% 55%, var(--chilli-bright), var(--chilli-deep) 75%, var(--ink));
  }

  .variety {
    position: absolute;
    left: 0;
    top: 758px;
    width: 532px;
    font-family: var(--slab);
    font-weight: 400;
    font-size: 28px;
    line-height: 34px;
    letter-spacing: 5px;
    color: var(--paper);
    transform: scaleX(1.6);
    transform-origin: center;
    white-space: nowrap;
  }
  .claim {
    position: absolute;
    left: 0;
    top: 806px;
    width: 532px;
    font-family: var(--gothic);
    font-size: 18px;
    line-height: 22px;
    letter-spacing: 3px;
    color: var(--chilli-bright);
  }

  .back {
    position: absolute;
    left: 826px;
    top: 0;
    width: 374px;
    height: 842px;
    background: var(--paper);
  }
  .back__heading {
    height: 74px;
    background: var(--ink);
    color: var(--paper);
    font-family: var(--slab);
    font-weight: 400;
    font-size: 15px;
    line-height: 18px;
    letter-spacing: 2px;
    padding: 31px 0 0 32px;
    white-space: nowrap;
  }
  .ingredients {
    padding: 20px 50px 0 27px;
    font-family: var(--gothic);
    font-size: 25px;
    line-height: 33.3px;
    text-align: justify;
    color: var(--ink);
  }
</style>
</head>
<body>
<main class="label">
  <div class="pepper-strip pepper-strip--left" role="img" aria-label="Repeating pattern of red chilli pepper drawings"></div>
  <div class="red-band red-band--left grunge"></div>

  <section class="front grunge">
    <div class="brand">
      <span class="brand__square"></span>
      <span class="brand__name">TOBY K'S</span>
    </div>
    <h1 class="product-title">
      <span>HAND</span>
      <span>MADE</span>
      <span class="hot">HOT</span>
      <span>SAUCE</span>
    </h1>
    <div class="chilli-art" role="img" aria-label="Red chilli pepper illustration"></div>
    <p class="variety">JALAPENO</p>
    <p class="claim">NO ADDED SUGARS</p>
  </section>

  <div class="red-band red-band--right grunge"></div>
  <div class="pepper-strip pepper-strip--right" role="img" aria-label="Repeating pattern of red chilli pepper drawings"></div>

  <section class="back">
    <h2 class="back__heading">INGREDIENTS</h2>
    <p class="ingredients">At vero eos et accusamus et iusto odio dignissimos ducimus qui bland itiis praesent ium volupt atum deleniti atque corrupti quos dolores et quas molestias except uri sint occaecati cupiditate non provident, similique sunt in culpa qui officia deserunt mollitia animi, id est laborum et dolorum fuga. Et harum quidem rerum facilis est et expedita distinctio. Nam libero tempore, cum soluta nobis est eligendi optio cumque nihil imped it quo minus id quod maxime placeat facere possimus, omnis voluptas assumenda est, omnis dolor repellendus. Temporibus autem quibusdam et aut officiis debitis aut rerum necessitatibus saepe eveniet ut</p>
  </section>
</main>
</body>
</html>
```